Business Card Design

Need a hot business card in wine colors something cool and mod please feel free to be , FUNKY and free with this .

Industry/Entity Type

Business

Contact Information for Business Card

LUMERA HAIR DESIGN 3182 w 9th st scottsdale az 85619 Custom modern hair design and custom color by MARCUS OBRIDGE 602-4168203 cell salon 480 -712-6084 email marcusobridge@quillpost.com hours wed thru sat 7am to 6pm.

Font styles to use
Other font styles liked:
• something fun and mod.

Colors
a54599
6b449b
1b1b1b
606060

Requirements
Must have
• Apointment reminder on flip side of card.
Should not have
• Nothing boring.

```html
<!DOCTYPE html>
<html lang="en">
<head>
<meta charset="utf-8">
<title>Lumera Hair Design – Business Card</title>
<link rel="stylesheet" href="https://fonts.googleapis.com/css2?family=Montserrat:wght@400;600;700&family=Questrial&display=swap">
<style>
  :root {
    --page: #f4f4f4;
    --card: #1b1b1b;
    --card-deep: #0e0e0e;
    --damask: #3a3a3a;
    --grey: #606060;
    --magenta: #c43bbb;
    --wine: #a54599;
    --violet: #6b449b;
    --band-text: #2b0f2a;
    --field: #ffffff;
  }
  * { box-sizing: border-box; margin: 0; padding: 0; }
  html, body {
    width: 1200px; height: 900px; overflow: hidden;
    background: var(--page);
  }
  .stage {
    width: 1200px; height: 900px;
    display: flex; align-items: center; justify-content: center; gap: 40px;
  }
  .card {
    position: relative;
    width: 540px; height: 310px;
    border-radius: 24px;
    background: var(--card);
    overflow: hidden;
    font-family: "Montserrat", Arial, sans-serif;
    color: var(--magenta);
  }
  .damask {
    position: absolute; inset: 0;
    background:
      radial-gradient(ellipse at 45% 85%, var(--damask) 0%, rgba(40,40,40,0.6) 35%, transparent 70%),
      linear-gradient(180deg, var(--card-deep) 0%, var(--card) 45%, #242424 100%);
  }
  .brand-name {
    position: absolute; left: 0; right: 0;
    font-family: "Questrial", Arial, sans-serif;
    font-weight: 400;
    color: var(--wine);
    text-align: center;
    letter-spacing: 1px;
  }
  /* Front */
  .front .brand-name { top: 52px; font-size: 40px; }
  .tagline-band {
    position: absolute; left: 0; right: 0; top: 128px; height: 26px;
    background: linear-gradient(90deg, var(--violet) 0%, var(--magenta) 55%, var(--violet) 100%);
    font-family: "Questrial", Arial, sans-serif;
    font-size: 16.5px; letter-spacing: 1.6px;
    color: var(--band-text);
    text-align: center; line-height: 26px;
  }
  .byline {
    position: absolute; left: 0; right: 0; top: 160px;
    text-align: center; font-size: 14px; color: var(--violet);
  }
  .stylist {
    position: absolute; left: 0; right: 0; top: 178px;
    text-align: center; font-size: 15px; font-weight: 700; letter-spacing: 2px;
  }
  .contact-list {
    position: absolute; left: 24px; top: 212px;
    list-style: none; font-size: 12.5px; line-height: 17px;
  }
  .contact-list li { display: flex; align-items: center; gap: 8px; }
  .contact-list svg { width: 11px; height: 11px; fill: var(--magenta); flex: none; }
  /* Back */
  .appointment-title {
    position: absolute; left: 0; right: 0; top: 32px;
    text-align: center; font-size: 15px; font-weight: 600; letter-spacing: 1.2px;
  }
  .field-label {
    position: absolute; font-size: 17px; font-weight: 600;
  }
  .field-box {
    position: absolute; height: 28px;
    background: var(--field);
    border: 2px solid var(--magenta);
  }
  .label-name { left: 26px; top: 86px; }
  .box-name   { left: 100px; right: 18px; top: 80px; }
  .label-date { left: 26px; top: 133px; }
  .box-date   { left: 100px; width: 170px; top: 127px; }
  .label-time { left: 280px; top: 127px; font-size: 15px; }
  .box-time   { left: 322px; right: 18px; top: 124px; }
  .hours {
    position: absolute; left: 0; right: 0; top: 210px;
    text-align: center; font-size: 15px; font-weight: 600;
  }
  .back .brand-name { top: auto; left: auto; bottom: 48px; right: 22px; font-size: 21px; }
</style>
</head>
<body>
<main class="stage">

  <section class="card front" aria-label="Business card front">
    <div class="damask" role="img" aria-label="Dark grey floral damask pattern background"></div>
    <h1 class="brand-name">LUMERA HAIR DESIGN</h1>
    <p class="tagline-band">Custom modern hair design and custom color</p>
    <p class="byline">by</p>
    <p class="stylist">MARCUS OBRIDGE</p>
    <ul class="contact-list">
      <li>
        <svg viewBox="0 0 12 12" aria-hidden="true"><rect x="3" y="0.5" width="6" height="11" rx="1.2"/><rect x="4" y="2" width="4" height="6.5" fill="#1b1b1b"/></svg>
        602-4168203
      </li>
      <li>
        <svg viewBox="0 0 12 12" aria-hidden="true"><path d="M2.2 0.8 4.3 3 3.3 4.6c.8 1.6 2.2 3 3.8 3.8l1.6-1 2.2 2.1-1.3 1.6C5.2 10.9 1 6.7.6 2.1z"/></svg>
        480 -712-6084
      </li>
      <li>
        <svg viewBox="0 0 12 12" aria-hidden="true"><path d="M0.5 2.5h11v7h-11z"/><path d="M0.8 2.8 6 7l5.2-4.2" stroke="#1b1b1b" stroke-width="1" fill="none"/></svg>
        marcusobridge@quillpost.com
      </li>
      <li>
        <svg viewBox="0 0 12 12" aria-hidden="true"><path d="M6 0.8 11.4 5.8H9.8v5.4H7.2V8H4.8v3.2H2.2V5.8H.6z"/></svg>
        3182 w 9th st scottsdale az 85619
      </li>
    </ul>
  </section>

  <section class="card back" aria-label="Business card back, appointment reminder">
    <div class="damask" role="img" aria-label="Dark grey floral damask pattern background"></div>
    <h2 class="appointment-title">Appointment</h2>
    <span class="field-label label-name">Name:</span>
    <div class="field-box box-name"></div>
    <span class="field-label label-date">Date:</span>
    <div class="field-box box-date"></div>
    <span class="field-label label-time">Time:</span>
    <div class="field-box box-time"></div>
    <p class="hours">hours wed thru sat 7am to 6pm</p>
    <p class="brand-name">LUMERA HAIR DESIGN</p>
  </section>

</main>
</body>
</html>
```